Book cover for a sci fi book called The Velvet Assembly

Dear Pixel Harbor team,

I would need a book cover design for my sci fi book, 'The Velvet Assembly'.

I will start by briefing you about the book's content, then I would like to advice you about a few possible book cover scenarios that I could imagine having for the book, and on which I would like to ask you to work on.

Book abstract:

The velvet assembly is a technically developed and spiritually evolved society from a distant galaxy.

Main location the actions take place: Planet Earth, globalized world, former Northern Germany, a new isolated high tech city at the sea, called Lees, inhabitants from everywhere, one government, one religion.
• Year: 2093
• The Velvet Assembly: solar system with 7 suns. The inhabitans of the velvet assembly have no physical body, only energetical bodies. Only when visiting Earth, they can incarnate at will.

The action starts on planet Earth, where a group of 4 people, two women and two males, who meet through different circumstances and decide to follow together a spiritual and philiosophical path towards self development and evolution. They meet an incarnated master from the velvet assembly who leads their path. At the end of the books, they reach a form of enlightment and transcende to The Velvet Assembly, they only come to know at the end the truth about the real origin of their master.

For the book cover, no matter what ideas you choose, please use max three predominant colors for that, red, yellow and orange. The book cover should inspire warmth.

Suggestions for the design:
- an abstract sun
- a cosmic view of the velvet assembly
- an abstractized design of a sacred geometry shape
- sun in the upper left corner, shining with visible rays on the whole surface of the book cover, a group of 4 people with the female old master sitting by their side in the lower right corner
- an out of the box Ufo, please choose for example an asymmetrical shape, definately not the usual flying sorcer, departing from the velvet assembly solar system, cosmic view from above
- PLEASE FEEL FREE TO BRAINSTROM ON YOUR OWN IDEAS BASED ON WHAT THE BOOK ABSTRACT INSPIRED YOU

For any questions, I am atbyour disposal.

I am looking forward to your design, thank you in advance for that.

Kind regards,
Mira

Target Market(s)

Sci Fi enthusiasts
Philosophers

Font styles to use
Serif

Colors
fbee3e
ffc214
faa54b
f37122
f04a50

Requirements
Must have
• For the book cover, no matter what ideas you choose, please use max three predominant colors for that, red, yellow and orange and/or any derived hues. The book cover should inspire warmth.
• Suggestions for the design:
• - an abstract sun
• - a cosmic view of the velvet assembly
• - an abstractized design of a sacred geometry shape
• - sun in the upper left corner, shining with visible rays on the whole surface of the book cover, a group of 4 people with the female old master sitting by their side in the lower right corner
• - an out of the box Ufo, please choose for example an asymmetrical shape, definately not the usual flying sorcer, departing from the velvet assembly solar system, cosmic view from above
• - PLEASE FEEL FREE TO BRAINSTROM ON YOUR OWN IDEAS BASED ON WHAT THE BOOK ABSTRACT INSPIRED YOU
Nice to have
• Minimalistic and modern design
Should not have
• dark or grey shades
• phtographs

```html
<!DOCTYPE html>
<html lang="en">
<head>
<meta charset="utf-8">
<title>The Velvet Assembly — Book Cover</title>
<link rel="stylesheet" href="https://fonts.googleapis.com/css2?family=Caladea:ital,wght@1,700&display=swap">
<style>
  :root {
    --cover-orange: #ef7124;
    --sun-yellow: #f5e53f;
    --glow-orange: #f59a2e;
  }
  html, body {
    margin: 0;
    padding: 0;
    overflow: hidden;
    background: var(--cover-orange);
  }
  .book-cover {
    position: relative;
    width: 848px;
    height: 1200px;
    overflow: hidden;
    background: var(--cover-orange);
  }
  .cosmic-artwork {
    position: absolute;
    left: 0;
    top: 0;
    width: 848px;
    height: 620px;
    background: radial-gradient(ellipse 520px 380px at 421px 190px,
      var(--sun-yellow) 0%,
      var(--glow-orange) 45%,
      var(--cover-orange) 100%);
  }
  .title {
    position: absolute;
    left: 44px;
    top: 610px;
    margin: 0;
    font-family: "Caladea", "Cambria", serif;
    font-style: italic;
    font-weight: 700;
    font-size: 110px;
    line-height: 155px;
    letter-spacing: 16px;
    color: var(--sun-yellow);
    text-transform: uppercase;
  }
  .title-line {
    display: block;
  }
  .author-name {
    position: absolute;
    left: 44px;
    top: 1078px;
    margin: 0;
    font-family: "Caladea", "Cambria", serif;
    font-style: italic;
    font-weight: 700;
    font-size: 28px;
    letter-spacing: 1px;
    color: var(--sun-yellow);
    text-transform: uppercase;
  }
</style>
</head>
<body>
  <main class="book-cover">
    <div class="cosmic-artwork" role="img" aria-label="Illustration of a solar system: a central yellow sun with planets on wide elliptical orbits"></div>

    <h1 class="title">
      <span class="title-line">The</span>
      <span class="title-line">Velvet</span>
      <span class="title-line">Assembly</span>
    </h1>
    <p class="author-name">Authors Name</p>
  </main>
</body>
</html>
```